Real Estate Fund Needs Flyer showing our current properties

We are a growing real estate fund and we want to show new investors the properties we currently own. There are 4 pictures with descriptions. Also there are quotes and notes regarding the fund throughout the flyer also. The main purpose is to attract new investors to the fund. Pictures are attached. The text in the example needs to be the same on the new design. There are 4 properties. The example only has 3. But Pic titled 517KBramt needs to have this text also:

318 W Marrow Ave., Liberty, MO 64071

The Quillby Residences consist of 20 units. They are located in downtown Liberty, Missouri, adjacent to the Historic Downtown Square. This convenient location is close to City and County offices, shopping, restaurants, and employment centers. Quillby Residences are only blocks from Dorrance Pike College. Liberty is a rapidly growing suburb of Kansas City, Missouri. It is a progressive city with expanding business development and new industry. Located just a few miles north of the Missouri River on Interstate I-35, it is among the largest and fastest growing suburbs in the area. Major employers in Liberty include the Vendrel distribution and operations headquarters for Tosklinfuel.

Target Market(s)

New investors

Industry/Entity Type

Real Estate

Requirements
Must have
• Sleek business like feel.
Nice to have
• Colors matching our brand. Unique backgrounds
• Our website: www.plumtidegroup.example
Should not have
• Our current design is attached. We do not like it at all. The colors aren't right and it's boring.

```html
<!DOCTYPE html>
<html lang="en">
<head>
<meta charset="utf-8">
<title>Plumtide Group – Recent Acquisitions</title>
<link href="https://fonts.googleapis.com/css2?family=Open+Sans:wght@400;600;700&family=Roboto+Condensed:wght@700&display=swap" rel="stylesheet">
<style>
:root{
  --brand-red:#8e1c1f;
  --brand-red-dark:#6e1215;
  --gold:#f3d27c;
  --ink:#333;
  --paper:#fff;
  --footer-bg:#ececec;
}
*{margin:0;padding:0;box-sizing:border-box}
html,body{width:849px;height:1200px;overflow:hidden;background:var(--paper)}
body{font-family:"Open Sans",Arial,sans-serif;color:var(--ink);position:relative}
.brand{position:absolute;left:28px;top:40px;width:290px;display:flex;align-items:center;gap:12px}
.brand-mark{width:30px;height:30px;background:var(--brand-red);flex:none}
.brand-name{font-weight:700;font-size:27px;color:var(--brand-red);line-height:1.1}
.brand-sub{position:absolute;left:70px;top:78px;font-size:15px;color:var(--brand-red);font-weight:700}
.hero-photo{position:absolute;left:0;top:205px;width:849px;height:395px;
  background:linear-gradient(180deg,#9fc3e6 0%,#c9dcef 28%,#8e5140 45%,#7a3e31 70%,#5f7a3d 88%,#4d6a2e 100%)}
.intro-panel{position:absolute;left:325px;top:0;width:524px;height:275px;background:var(--brand-red);padding:20px 24px;color:#fff}
.intro-title{color:var(--gold);font-size:22px;font-weight:700;margin-bottom:12px}
.intro-text{font-size:13.4px;line-height:1.45}
.intro-text strong{font-weight:700}
.listings{position:absolute;left:22px;top:614px;width:805px;display:flex;gap:15px}
.listing{width:190px;flex:none}
.listing-photo{position:relative;height:160px}
.listing-caption{position:absolute;left:0;right:0;bottom:0;background:var(--brand-red);color:#fff;
  font-family:"Roboto Condensed",Arial,sans-serif;font-weight:700;font-size:10.5px;line-height:1.3;padding:4px 6px;text-transform:uppercase}
.listing-text{font-size:10px;line-height:1.45;margin-top:9px;color:#444}
.photo-maple{background:linear-gradient(180deg,#a8c6e3 0%,#b05a3e 40%,#8a4030 70%,#6d8a44 100%)}
.photo-bramt{background:linear-gradient(180deg,#8fb4dc 0%,#c8b79a 45%,#a38f6c 70%,#7d8c5a 100%)}
.photo-tidewell{background:linear-gradient(180deg,#a6c4e4 0%,#d9c5a4 45%,#b99a6f 72%,#6f8a48 100%)}
.photo-quillby{background:linear-gradient(180deg,#a2c2e2 0%,#a65a44 42%,#7f3c2e 70%,#5e7d3c 100%)}
.footer{position:absolute;left:0;top:1120px;width:849px;height:80px;background:var(--footer-bg);display:flex;justify-content:space-between;align-items:center;padding:0 28px}
.footer-contact{font-size:13.5px;font-weight:700;color:var(--brand-red-dark);line-height:1.5}
.footer-web{font-size:12px;color:#444;line-height:1.5}
.footer-web strong{color:var(--brand-red);font-size:13.5px}
</style>
</head>
<body>
  <div class="brand"><span class="brand-mark"></span><span class="brand-name">PLUMTIDE GROUP</span></div>
  <div class="brand-sub">Real Estate Fund</div>

  <div class="hero-photo" role="img" aria-label="Photo of a three-storey red brick apartment building with white porches and green lawn"></div>

  <section class="intro-panel">
    <h1 class="intro-title">Recent Acquisitions By Plumtide Group</h1>
    <p class="intro-text">Our purchasing phase has commenced! Below are the current properties owned by the fund. Our team has experience in almost all parts of the US and is working hard to acquire additional properties as soon as possible.<br>As an investor, you not only own a piece of everything currently owned, but every future acquisition! The quicker you buy in, the quicker you start receiving dividend payouts. <strong>Our motto:</strong> Why own one property when you can own a piece of many with no headaches?</p>
  </section>

  <section class="listings">
    <article class="listing">
      <div class="listing-photo photo-maple" role="img" aria-label="Photo of a red brick apartment building">
        <div class="listing-caption">812 Alder Blvd, Kansas City, MO 64124</div>
      </div>
      <p class="listing-text">This property consists of three, eight-unit, walk-up style apartment buildings, totaling twenty-four units. All three buildings and all units have been completely renovated and the total building area is 13,782 SF. It is located a mere few minutes from the booming downtown Riverside Lights District. At purchase the building was 100% occupied. With its close proximity to both downtown and the Midtown Institute of Health Sciences, a steady increase in both rents and appreciation is expected.</p>
    </article>
    <article class="listing">
      <div class="listing-photo photo-bramt" role="img" aria-label="Photo of a beige fourplex apartment building">
        <div class="listing-caption">4418 K Bramt Ave., Las Vegas, NV 89108</div>
      </div>
      <p class="listing-text">This beautiful building has four units and is located at 4418 K Bramt Ave, Las Vegas, NV 89108. It recently went through a complete remodel that includes washer/dryer units and dual-pane energy efficient windows. The property is located close to the Desert Ridge Technology Center and will devour some of the highest rents for the area. The nearest schools are Harlow Pine Elementary School and the Westbrook Memorial High School.</p>
    </article>
    <article class="listing">
      <div class="listing-photo photo-tidewell" role="img" aria-label="Photo of a two-storey stucco condominium building">
        <div class="listing-caption">2107 Tidewell Dr., Las Vegas, NV 89128</div>
      </div>
      <p class="listing-text">This luxury condominium is housed within a great community of buildings. Amenities include: private balconies, new appliances, washer/dryer in each unit, community pool, exercise room, jogging trail, and a playground with a park. Schools in the area are: The Calder Roe Elementary School and the Westbrook Memorial High School. The desirable location as well as the vast amenities of this property not only make it easy to keep at 100% occupancy, but should also add to the appreciation potential.</p>
    </article>
    <article class="listing">
      <div class="listing-photo photo-quillby" role="img" aria-label="Photo of a brick apartment building in downtown Liberty">
        <div class="listing-caption">318 W Marrow Ave., Liberty, MO 64071</div>
      </div>
      <p class="listing-text">The Quillby Residences consist of 20 units. They are located in downtown Liberty, Missouri, adjacent to the Historic Downtown Square. This convenient location is close to City and County offices, shopping, restaurants, and employment centers. Quillby Residences are only blocks from Dorrance Pike College. Liberty is a rapidly growing suburb of Kansas City, Missouri. It is a progressive city with expanding business development and new industry. Located just a few miles north of the Missouri River on Interstate I-35, it is among the largest and fastest growing suburbs in the area. Major employers in Liberty include the Vendrel distribution and operations headquarters for Tosklinfuel.</p>
    </article>
  </section>

  <footer class="footer">
    <div class="footer-contact">2280 Harwick Blvd Ste 410 Los Angeles, CA 90036<br>(877) 555-0142 | (323) 555-0187</div>
    <div class="footer-web">Additional pictures and properties will be added as they are purchased.<br><strong>PLEASE VIEW www.plumtidegroup.example</strong></div>
  </footer>
</body>
</html>
```